Business Card Design

We are a new motor lodge in Hamilton NZ. Providing luxury accommodation and excellent service is the core of our business. We are looking for a different business card to capture the eye once in there hand. We have quite a lot of different clientele, corporate, travellers passing by plus we are positioned by two main hospitals so we have a lot of guests staying from there.
The existing card we have has a bed in the background with our logo. Does not stand out too much.

Maisie

To our final designers we will be making a decision today. we will be intouch

Target Market(s)

Quite a variety from single travellers to families

Industry/Entity Type

Accommodation

Contact Information for Business Card

Pelora Motor Lodge Maisie & Gareth Lund
18 Wirimu Crescent Hamilton 3204
Freephone 0800 519 364
Phone 07 946 3381
Fax 07 9463382
info@peloramotorlodge-example.co.nz
www.peloramotorlodge-example.co.nz

Colors

Designer to choose colors to be used in the design.

Requirements
Must have
• Name:
Address:
Phone Numbers:
Web and Email Addresses.
Pelora Logo
map on the back of our positioning
Nice to have
• Something styley and eyecatching have included a couple of photos of the Motor Lodge

```html
<!DOCTYPE html>
<html lang="en">
<head>
<meta charset="utf-8">
<title>Pelora Motor Lodge – Business Card</title>
<link href="https://fonts.googleapis.com/css2?family=Arimo:wght@400;700&display=swap" rel="stylesheet">
<style>
  :root {
    --backdrop: #e9e6e1;
    --card: #1c1c1c;
    --sky: #8cc6ec;
    --ink: #ffffff;
    --rule: #8a8a8a;
  }
  * { margin: 0; padding: 0; box-sizing: border-box; }
  html, body {
    width: 1200px; height: 1023px; overflow: hidden;
    background: var(--backdrop);
    font-family: "Arimo", Arial, sans-serif;
  }
  .sheet {
    width: 1200px; height: 1023px;
    display: flex; flex-direction: column; align-items: center; justify-content: center;
    gap: 60px;
  }
  .card {
    position: relative;
    width: 700px; height: 400px;
    background: var(--card);
    box-shadow: 0 6px 18px rgba(0,0,0,.25);
    overflow: hidden;
  }
  .wordmark {
    font-weight: 700; color: var(--sky);
    text-transform: uppercase; line-height: 1; white-space: nowrap;
  }

  /* Front */
  .card-front .accent-band {
    position: absolute; left: 0; right: 0; bottom: 0; height: 14px;
    background: var(--sky);
  }
  .card-front .wordmark {
    position: absolute; left: 60px; top: 64px;
    font-size: 40px; letter-spacing: 1px;
  }
  .card-front .wordmark-rule {
    position: absolute; left: 60px; top: 122px; width: 470px; height: 1px;
    background: var(--rule);
  }
  .owner-block {
    position: absolute; left: 20px; width: 320px; top: 176px;
    text-align: right; color: var(--ink); font-size: 15px; line-height: 1.5;
    white-space: nowrap;
  }
  .owner-block .owners { color: var(--sky); font-weight: 700; font-size: 17px; }
  .owner-block .web { margin-top: 14px; }
  .column-divider {
    position: absolute; left: 358px; top: 150px; width: 1px; height: 118px;
    background: var(--rule);
  }
  .contact-list {
    position: absolute; left: 374px; top: 152px;
    list-style: none; color: var(--ink); font-size: 15px; line-height: 1.75;
    white-space: nowrap;
  }
  .contact-list li { display: flex; align-items: center; gap: 8px; }
  .contact-list svg { width: 13px; height: 13px; fill: var(--sky); flex: none; }

  /* Back */
  .card-back {
    display: flex; flex-direction: column; align-items: center; justify-content: center;
  }
  .card-back .wordmark { font-size: 50px; letter-spacing: 2px; }
  .card-back .wordmark-rule {
    width: 560px; height: 1px; margin-top: 18px;
    background: var(--rule);
  }
</style>
</head>
<body>
<main class="sheet">
  <section class="card card-front">
    <div class="wordmark">Pelora Motor Lodge</div>
    <div class="wordmark-rule"></div>
    <div class="owner-block">
      <p class="owners">Maisie &amp; Gareth Lund</p>
      <p>18 Wirimu Crescent</p>
      <p>Hamilton 3204</p>
      <p class="web">www.peloramotorlodge-example.co.nz</p>
    </div>
    <div class="column-divider"></div>
    <ul class="contact-list">
      <li><svg viewBox="0 0 16 16"><path d="M3 1l3 3-1.5 2a9 9 0 005.5 5.5L12 10l3 3-2 2C7 15 1 9 1 3z"/></svg>0800 519 364 (Free Phone)</li>
      <li><svg viewBox="0 0 16 16"><path d="M3 1l3 3-1.5 2a9 9 0 005.5 5.5L12 10l3 3-2 2C7 15 1 9 1 3z"/></svg>07 946 3381</li>
      <li><svg viewBox="0 0 16 16"><path d="M4 1h7v4H4zM1 6h14v8H1zm3 2v2h8V8z"/></svg>07 9463382</li>
      <li><svg viewBox="0 0 16 16"><path d="M1 3h14v10H1zm1 1v1l6 4 6-4V4z"/></svg>info@peloramotorlodge-example.co.nz</li>
    </ul>
    <div class="accent-band"></div>
  </section>
  <section class="card card-back">
    <div class="wordmark">Pelora Motor Lodge</div>
    <div class="wordmark-rule"></div>
  </section>
</main>
</body>
</html>
```